Flyer Design

We are a property company and need attractive flyers that will grab peoples attention. We want them to be bold but simple and not too busy. I attach a draft and also our logo. We will print in A5 size.
Thank you & I look forward to receiving designs.

Industry/Entity Type

It Company

```html
<!DOCTYPE html>
<html lang="en">
<head>
<meta charset="utf-8">
<title>Kea Developments – Subdivision Flyer</title>
<link href="https://fonts.googleapis.com/css2?family=Alegreya+Sans:wght@400;500&display=swap" rel="stylesheet">
<style>
  :root {
    --page-bg: #eceae6;
    --paper: #ffffff;
    --brand-red: #a9352b;
    --brand-brown: #3a1b15;
    --accent-line: #b8412f;
    --timber-light: #f1ece3;
    --timber-mid: #e2d8c8;
    --timber-ink: #8e6440;
    --info-bg: #e3e3e3;
    --body-ink: #1e1e1e;
    --link-red: #b2342a;
    --footer-ink: #f4f1ec;
  }
  * { box-sizing: border-box; margin: 0; padding: 0; }
  html, body {
    width: 1200px;
    height: 1000px;
    overflow: hidden;
    background: var(--page-bg);
    font-family: "Alegreya Sans", sans-serif;
  }
  .flyer {
    position: absolute;
    left: 70px;
    top: 125px;
    width: 1060px;
    height: 750px;
    background: var(--paper);
    padding: 16px 16px 28px;
    display: flex;
    flex-direction: column;
  }
  .rule-band {
    height: 22px;
    background: var(--brand-brown);
    position: relative;
  }
  .rule-band::after {
    content: "";
    position: absolute;
    left: 0; right: 0;
    height: 3px;
    background: var(--accent-line);
  }
  .rule-band--top::after { top: 13px; }
  .rule-band--bottom::after { top: 6px; }
  .hero {
    height: 358px;
    background: var(--brand-red);
    display: flex;
    justify-content: center;
  }
  .hero__panel {
    width: 510px;
    height: 100%;
    background: linear-gradient(100deg, var(--timber-light) 0%, var(--timber-mid) 45%, var(--timber-light) 70%, var(--timber-mid) 100%);
    display: flex;
    align-items: center;
    justify-content: center;
  }
  .brand-name {
    font-size: 44px;
    font-weight: 500;
    letter-spacing: 2px;
    color: var(--timber-ink);
    text-transform: uppercase;
  }
  .info {
    flex: 1;
    background: var(--info-bg);
    color: var(--body-ink);
    text-align: center;
    font-size: 21px;
    line-height: 1.2;
    padding: 20px 20px 0;
    letter-spacing: 0.3px;
  }
  .info p { margin-bottom: 20px; }
  .info .contact { margin-bottom: 0; }
  .info a { color: var(--link-red); text-decoration: none; }
  .site-footer {
    height: 62px;
    background: var(--brand-brown);
    color: var(--footer-ink);
    display: flex;
    align-items: center;
    justify-content: center;
    font-size: 26px;
    letter-spacing: 1.5px;
  }
</style>
</head>
<body>
  <main class="flyer">
    <div class="rule-band rule-band--top"></div>
    <section class="hero">
      <div class="hero__panel" role="img" aria-label="Light timber woodgrain panel behind the company name">
        <span class="brand-name">Kea Developments</span>
      </div>
    </section>
    <div class="rule-band rule-band--bottom"></div>
    <section class="info">
      <p>Are you a homeowner looking for financial freedom while been able to keep your own home?</p>
      <p>Are you struggling to pay your mortgage?</p>
      <p>KEA specialise in subdivisions including finance and management.</p>
      <p class="contact">Call 021 555 0147 or email <a href="mailto:info@keasubdivisions.com">info@keasubdivisions.com</a> for more information<br>or to find out if your property is suitable for subdivision in Auckland.</p>
    </section>
    <footer class="site-footer">www.keasubdivisions.com</footer>
  </main>
</body>
</html>
```